Design an Outstanding flyer for my company.

I need a flyer designed for our window tinting company based in Brisbane Queensland Australia. The flyer will be targeting Home tinting. We also do mobile car tinting. Something in regards to this could be incorporated into the flyer as well.
I want it to be 2 sided DL size. Black background.
It really needs to Pop, and be a real attention getter.
It needs to be easy to read.
I have provided a mock up with the info on it from our marketing company. It will need a spellcheck etc to make sure everything is correct.
Everything about it can be changed however you like.
I have also included the company logo.

Lets see what you've got!

Target Market(s)

Home Owners

Industry/Entity Type

Home Improvement

Font styles to use
Other font styles liked:
• Duan Penh

Requirements
Must have
• All the information on the mock up. Clear and easy to read.
• Must Stand Out!

```html
<!DOCTYPE html>
<html lang="en">
<head>
<meta charset="utf-8">
<title>Home Window Tinting Flyer</title>
<link rel="stylesheet" href="https://fonts.googleapis.com/css2?family=Tinos:wght@400;700&family=Lato:wght@400;700&family=Archivo+Black&display=swap">
<style>
  :root {
    --ink: #000000;
    --paper: #ffffff;
    --gold: #c9a13a;
    --gold-deep: #c49a2a;
    --gold-light: #e8d434;
    --yellow: #f2e41c;
    --dark-text: #141414;
    --logo-bg: #0c0c0c;
  }
  * { box-sizing: border-box; margin: 0; padding: 0; }
  html, body { width: 1200px; height: 1200px; overflow: hidden; background: var(--paper); }
  .canvas { position: relative; width: 1200px; height: 1200px; }

  .flyer {
    position: absolute; top: 34px; width: 535px; height: 1100px;
    background: var(--ink); overflow: hidden;
  }
  .flyer--front { left: 55px; }
  .flyer--back { left: 625px; }

  .abs { position: absolute; }
  .line { white-space: nowrap; display: block; }

  .headline { left: 51px; width: 450px; }
  .headline .heat { font-family: "Tinos", serif; font-weight: 700; font-size: 55px; color: var(--gold); line-height: 50px; letter-spacing: -0.5px; }
  .headline .uv { font-family: "Lato", sans-serif; font-size: 41px; color: var(--paper); line-height: 46px; letter-spacing: -1px; }
  .headline .money { font-family: "Tinos", serif; font-weight: 700; font-size: 66px; color: var(--yellow); line-height: 58px; letter-spacing: -0.5px; }
  .headline .privacy { font-family: "Tinos", serif; font-size: 45px; color: var(--paper); line-height: 56px; }

  .benefits {
    left: 55px; width: 430px;
    font-family: "Lato", sans-serif; font-size: 15.6px; line-height: 21.6px;
    color: var(--paper); text-align: justify;
  }

  .band { left: 0; width: 535px; }

  .reasons { font-family: "Tinos", serif; color: var(--dark-text); }
  .reasons .big { font-weight: 700; font-size: 40px; line-height: 44px; }
  .reasons .mid { font-size: 33px; line-height: 42px; color: var(--paper); }
  .reasons .bold { font-weight: 700; font-size: 37px; line-height: 46px; }

  .reasons-box {
    left: 54px; top: 47px; width: 437px; height: 132px;
    border-radius: 12px;
    background: linear-gradient(100deg, var(--gold-deep), var(--gold-light) 55%, var(--gold-deep));
    padding: 14px 0 0 30px;
  }
  .reasons-box .big { font-size: 39px; line-height: 40px; color: var(--paper); }
  .reasons-box .mid { font-size: 29px; line-height: 30px; color: var(--dark-text); }
  .reasons-box .bold { font-size: 31px; line-height: 34px; }

  .call { font-family: "Tinos", serif; }
  .call .lead { font-weight: 700; font-size: 27.5px; line-height: 34px; letter-spacing: 0.3px; }
  .call .now { font-family: "Lato", sans-serif; font-size: 30px; line-height: 36px; letter-spacing: -0.5px; color: var(--paper); }
  .flyer--front .call .lead { color: var(--yellow); }
  .flyer--back .call .lead { color: var(--dark-text); }

  .contact {
    height: 81px; width: 438px; border-radius: 12px;
    background: linear-gradient(100deg, var(--gold-deep), var(--gold-light) 55%, var(--gold-deep));
    padding: 2px 0 0 46px; color: var(--dark-text);
  }
  .contact .row { display: flex; align-items: baseline; gap: 10px; height: 40px; white-space: nowrap; }
  .contact .label { font-family: "Tinos", serif; font-weight: 700; font-size: 25px; }
  .contact .number { font-family: "Archivo Black", sans-serif; font-size: 36px; letter-spacing: 2px; line-height: 40px; }

  .brand {
    width: 378px; height: 128px; background: var(--logo-bg);
    display: flex; align-items: center; justify-content: center; gap: 14px;
  }
  .brand .dot { width: 34px; height: 34px; border-radius: 50%; background: var(--gold); }
  .brand .name { font-family: "Tinos", serif; font-weight: 700; font-size: 34px; color: var(--gold); letter-spacing: 1px; }
</style>
</head>
<body>
<main class="canvas">

  <!-- Front side -->
  <section class="flyer flyer--front">
    <div class="abs headline" style="top:45px;">
      <span class="line heat">KEEP HEAT OUT</span>
      <span class="line uv">BLOCK 99.9% UV RAYS</span>
      <span class="line money">SAVE MONEY</span>
      <span class="line privacy">INCREASE PRIVACY</span>
    </div>

    <p class="abs benefits" style="top:258px;">reduce glare. reduce energy costs. control the amount of light entering your home. reduce carbon footprint. make home more beautiful. eliminate home hot spots. protect against broken glass. regulate energy. protects upholstery. improve effectiveness of roof insulation. improve health. reduces interior floor fading. eliminate need for blinds. strengthen your windows. insulate in winter. affordable. improve health. reduces interior floor fading. eliminate need for blinds. strengthen your windows. insulate in</p>

    <svg class="abs band" style="top:430px;" width="535" height="320" viewBox="0 0 535 320" aria-hidden="true">
      <defs>
        <linearGradient id="bandFront" x1="0" y1="0" x2="1" y2="0">
          <stop offset="0" stop-color="#c49a2a"/>
          <stop offset="0.6" stop-color="#ebdb34"/>
          <stop offset="1" stop-color="#c9a22c"/>
        </linearGradient>
      </defs>
      <path d="M0 67 Q300 110 535 8 L535 210 Q330 310 0 300 Z" fill="#ffffff"/>
      <path d="M0 72 Q300 112 535 16 L535 190 Q330 300 0 290 Z" fill="url(#bandFront)"/>
    </svg>

    <div class="abs reasons" style="left:57px; top:530px;">
      <span class="line big">20 REASONS WHY</span>
      <span class="line mid">HOME WINDOW TINTING</span>
      <span class="line bold">IS PERFECT FOR YOU</span>
    </div>

    <div class="abs call" style="left:46px; top:774px;">
      <span class="line lead">CALL BRISBANE’S LEADER IN</span>
      <span class="line now">HOME WINDOW TINTING NOW</span>
    </div>

    <div class="abs contact" style="left:46px; top:874px;">
      <div class="row"><span class="label">TEL:</span><span class="number">07 3900 1847</span></div>
      <div class="row"><span class="label">SMS:</span><span class="number">0400 572 918</span></div>
    </div>

    <div class="abs brand" style="left:74px; top:958px;">
      <span class="dot"></span><span class="name">SUNLINE WINDOW TINTING</span>
    </div>
  </section>

  <!-- Back side -->
  <section class="flyer flyer--back">
    <div class="abs reasons reasons-box">
      <span class="line big">20 REASONS WHY</span>
      <span class="line mid">HOME WINDOW TINTING</span>
      <span class="line bold">IS PERFECT FOR YOU</span>
    </div>

    <div class="abs headline" style="top:207px; left:52px;">
      <span class="line heat">KEEP HEAT OUT</span>
      <span class="line uv">BLOCK 99.9% UV RAYS</span>
      <span class="line money">SAVE MONEY</span>
      <span class="line privacy">INCREASE PRIVACY</span>
    </div>

    <p class="abs benefits" style="top:424px; left:57px;">reduce glare. reduce energy costs. control the amount of light entering your home. reduce carbon footprint. make home more beautiful. eliminate home hot spots. protect against broken glass. regulate energy. protects upholstery. improve effectiveness of roof insulation. improve health. reduces interior floor fading. eliminate need for blinds. strengthen your windows. insulate in winter. affordable. improve health. reduces interior floor fading. eliminate need for blinds. strengthen your windows. insulate in</p>

    <svg class="abs band" style="top:620px;" width="535" height="250" viewBox="0 0 535 250" aria-hidden="true">
      <defs>
        <linearGradient id="bandBack" x1="0" y1="0" x2="1" y2="0">
          <stop offset="0" stop-color="#c49a2a"/>
          <stop offset="0.55" stop-color="#ebdb34"/>
          <stop offset="1" stop-color="#c9a22c"/>
        </linearGradient>
      </defs>
      <path d="M0 10 Q260 85 535 52 L535 240 Q220 245 0 146 Z" fill="#ffffff"/>
      <path d="M0 18 Q260 92 535 58 L535 233 Q220 238 0 138 Z" fill="url(#bandBack)"/>
    </svg>

    <div class="abs call" style="left:54px; top:717px;">
      <span class="line lead">CALL BRISBANE’S LEADER IN</span>
      <span class="line now">HOME WINDOW TINTING NOW</span>
    </div>

    <div class="abs contact" style="left:59px; top:891px;">
      <div class="row"><span class="label">TEL:</span><span class="number">07 3900 1847</span></div>
      <div class="row"><span class="label">SMS:</span><span class="number">0400 572 918</span></div>
    </div>

    <div class="abs brand" style="left:103px; top:974px;">
      <span class="dot"></span><span class="name">SUNLINE WINDOW TINTING</span>
    </div>
  </section>

</main>
</body>
</html>
```